New web and ecommerce design for The Brindle Works

--Background--

The Brindel Works is uk biggest supplier of Coasters and coinage products. We sell mostly to the UK but have customers all around the world. We are now in need of a new website/e-commerce platform and design.

Our current site http://brindelworks.example is VERY old and outdated.

The new site should be a e-commerce site with responsive design that will look good on all handheld devices.

The customer base is both retail, b2b, and artists so it should be something that appeals to everyone and that is suitable for 2015 and forward. New and fresh.

We need a front page and one product page.

--Design--
We are looking for a new fresh design that will stand out of the crowd. We like clean and slick design that is not to cluttered. We like people and design that think a little outside the box and find new ways and design. The design should look just as good on handheld devices as on normal computers.

Some sample sites that we have been looking at

http://www.velmaronstore.example/se_en/ - We like the clean look and navigation
Attached design is also very nice (even though for a different segment)

We like nice images of live people interacting, using the products

--Competitors site--
http://www.quillbarrowglobal.example/shop-by-range/placemats-and-coasters.html To traditional but overwise nice

--Rewamp of logo--
We would also like a logo created in this. Name: The Brindel Works

--Video--
We would like to have much videos on our pages so the design must take this into account and give some samples of this.

--Handheld devices - Responsive design--
The store should look good and be adapted to work well on all handheld devices like iphone, ipad and similar android and google based systems. This is a vital part of the solution and we are looking for a solution that automatically adapts when putting in new information and images.

--PSD files--
We would like all PSD files for main page and one product page to be delivered

Target Market(s)

consumers and prestigious clients such as Harrowmere Hall and Dunstreel Court

Industry/Entity Type

Gift Shop

Number of Pages Required

2 page

Requirements
Must have
• logo
Nice to have
• clean look and feel

```html
<!DOCTYPE html>
<html lang="en">
<head>
<meta charset="utf-8">
<title>The Brindel Works — Home</title>
<link href="https://fonts.googleapis.com/css2?family=Roboto+Slab:wght@400;700&family=Roboto+Condensed:wght@400&family=Arimo:wght@400;700&display=swap" rel="stylesheet">
<style>
:root{
  --red:#b30d0d;
  --red-dark:#8f0a0a;
  --ink:#222;
  --muted:#555;
  --line:#cfcfcf;
  --green:#a3cc33;
  --orange:#ee7f00;
  --charcoal:#333;
  --footer:#1f1f1f;
  --hero-bg:#d4d4d4;
  --badge:#e6e6e6;
}
*{box-sizing:border-box;margin:0;padding:0}
html,body{width:834px;height:1200px;overflow:hidden;background:#fff}
body{position:relative;font-family:"Arimo",Arial,sans-serif;color:var(--ink);font-size:9px}
.abs{position:absolute}

/* header */
.topline{left:0;top:0;width:834px;height:2px;background:#2a1a1a}
.account{right:115px;top:7px;display:flex;font-size:9.5px;color:#333}
.account span{display:flex;align-items:center;gap:5px;padding:0 12px}
.account span+span{border-left:1px solid #ccc;height:20px}
.logo{left:105px;top:38px;font-family:"Roboto Slab",serif;font-weight:700;font-size:21px;color:var(--red);letter-spacing:.3px}
.cart{left:470px;top:40px;display:flex;gap:6px;align-items:flex-start}
.cart b{display:block;font-family:"Roboto Condensed",sans-serif;color:var(--red);font-size:12.5px;font-weight:400}
.cart small{font-size:7px;color:#777}
.badge{left:656px;top:38px;width:64px;height:32px;border-radius:4px;background:var(--badge)}

/* nav */
.nav{left:0;top:80px;width:834px;height:33px;background:var(--red)}
.nav ul{list-style:none;display:flex;margin-left:104px;height:33px}
.nav li{color:#fff;font-size:11px;line-height:33px;padding:0 9.5px;letter-spacing:.2px}
.nav li.active{background:#3a3a3a;padding:0 19px}

/* hero */
.hero{left:0;top:113px;width:834px;height:261px;background:var(--hero-bg)}
.hero-art{left:0;top:113px;width:465px;height:261px;background:linear-gradient(120deg,#a01818 0%,#2a2a3a 35%,#e8dcc0 55%,#1a1a1a 75%,#5a2030 100%)}
.hero-copy{right:120px;top:170px;text-align:right;font-family:"Roboto Condensed",sans-serif;color:var(--red);font-size:21px;line-height:23.5px}
.arrow{top:222px;width:24px;height:24px;background:#2a2a2a;display:flex;align-items:center;justify-content:center}

/* section title */
.section-head{left:0;top:390px;width:834px;text-align:center}
.section-head h2{font-family:"Roboto Slab",serif;font-weight:400;font-size:17px;color:var(--ink)}
.section-head h2 em{font-style:normal;color:var(--red)}
.section-head p{font-size:9.5px;margin-top:4px}
.rule{left:244px;top:434px;width:340px;height:1px;background:var(--line)}
.stars{left:395px;top:428px;letter-spacing:2px;font-size:10px;color:#333;background:#fff;padding:0 2px}

/* tiles */
.tile{position:absolute;overflow:hidden}
.tile h3{font-family:"Roboto Slab",serif;font-weight:400;font-size:12px;margin:20px 0 14px 15px}
.tile p{font-size:8.2px;line-height:13px;margin:0 10px 0 14px}
.go{position:absolute;right:8px;bottom:6px;width:13px;height:13px;border:1px solid currentColor;border-radius:50%}
.go::after{content:"";position:absolute;left:3px;top:3.5px;width:3.5px;height:3.5px;border-top:1px solid currentColor;border-right:1px solid currentColor;transform:rotate(45deg)}
.photo{position:absolute}
.caption{position:absolute;left:0;bottom:0;width:100%;height:22px;background:var(--red);color:#fff;font-family:"Roboto Slab",serif;font-size:10.5px;line-height:22px;padding-left:4px}
.caption .go{color:#fff;bottom:4px;right:6px}

/* welcome */
.welcome{left:105px;top:848px;width:410px}
.block-title{font-family:"Roboto Slab",serif;font-weight:400;font-size:15.5px;padding-bottom:4px;border-bottom:1px dashed #bbb}
.block-title em{font-style:normal;color:var(--red)}
.welcome p{font-size:8.2px;line-height:12px;color:var(--muted);margin-top:6px}
.welcome .strong{font-weight:700;color:#444}
.welcome .tagline{color:var(--red);font-size:11px;margin-top:8px}
.welcome .more{text-decoration:underline;color:#333;font-size:9px;margin-top:14px}
.divider{left:529px;top:854px;height:158px;border-left:1px dashed #ccc}
.inquiry{left:545px;top:848px;width:185px}
.field{height:21px;border:1px solid #ddd;margin-top:3px;font-size:8px;color:#aaa;padding:5px 7px}
.field.msg{height:34px}
.first{margin-top:12px}
.submit{margin-top:4px;width:77px;height:21px;background:var(--red);color:#fff;font-size:12.5px;text-align:center;line-height:21px}

/* footer */
.footer{left:0;top:1039px;width:834px;height:131px;background:var(--footer);color:#ddd}
.footnav{position:absolute;left:104px;top:16px;display:flex;font-size:9.5px;color:#eee}
.footnav span{padding:0 7px;border-left:1px solid #666}
.footnav span:first-child{border:none;padding-left:5px}
.foot-rule{position:absolute;left:104px;top:41px;width:626px;height:1px;background:#3a3a3a}
.address{position:absolute;left:105px;top:58px;font-size:10px;line-height:19px}
.contacts{position:absolute;left:248px;top:56px;font-size:9.5px;line-height:21px}
.contacts div{display:flex;align-items:center;gap:8px}
.email-in{position:absolute;left:398px;top:56px;width:160px;height:23px;border:1px solid #555;font-size:9.5px;padding:5px 6px;color:#eee}
.subscribe{position:absolute;left:398px;top:88px;width:160px;height:23px;background:#5c5c5c;color:#fff;font-size:12.5px;text-align:center;line-height:23px}
.foot-logo{position:absolute;left:600px;top:64px;width:125px;text-align:center;font-family:"Roboto Slab",serif;font-weight:700;font-size:15px;color:#9a9a9a;line-height:19px}
.legal{left:0;top:1170px;width:834px;height:30px;background:var(--red);color:#fff;font-size:8px}
.legal p{position:absolute;left:105px;top:10px}
.social{position:absolute;left:642px;top:5px;display:flex;gap:7px}
.social span{width:21px;height:21px;border-radius:50%;background:#fff}
</style>
</head>
<body>

<div class="abs topline"></div>
<div class="abs account">
  <span><svg width="10" height="10" viewBox="0 0 10 10"><path d="M5 1 L8 4 H6 V7 H4 V4 H2 Z M1 8 H9 V9 H1Z" fill="#333"/></svg>Register</span>
  <span><svg width="10" height="10" viewBox="0 0 10 10"><circle cx="5" cy="5" r="3.8" fill="none" stroke="#333" stroke-width="1.2"/><path d="M3 5 H7 M5.5 3.5 L7 5 L5.5 6.5" stroke="#333" fill="none"/></svg>Login</span>
</div>
<div class="abs logo">The Brindel Works</div>
<div class="abs cart">
  <svg width="34" height="30" viewBox="0 0 34 30"><path d="M1 3 H6 L10 19 H28 L31 7 H8" fill="none" stroke="#b30d0d" stroke-width="2.4"/><path d="M10 11 H29 M10 15 H28" stroke="#b30d0d" stroke-width="1.6"/><circle cx="12" cy="25" r="2.4" fill="#b30d0d"/><circle cx="26" cy="25" r="2.4" fill="#b30d0d"/></svg>
  <div><b>SHOPPING CART:</b><small>Now in Your Cart <strong style="color:#333">0 Items</strong></small></div>
</div>
<div class="abs badge" role="img" aria-label="Security certificate badge"></div>

<nav class="abs nav">
  <ul>
    <li class="active">HOME</li><li>FOR INDIVIDUALS</li><li>FOR BUSINESSES</li><li>FOR SHOPS</li><li>FOR CLUBS</li><li>FOR ARTISTS</li><li>CONTACT US</li>
  </ul>
</nav>

<div class="abs hero"></div>
<div class="abs hero-art" role="img" aria-label="Fan of printed custom drink coasters for bars, nightclubs and events"></div>
<div class="abs hero-copy">We Specialise In Custom<br>Manufacture And Can offer<br>Our Products Customised<br>For Virtually Any Task<br>or Occasion</div>
<div class="abs arrow" style="left:6px"><svg width="8" height="10"><path d="M6 1 L2 5 L6 9" stroke="#fff" stroke-width="2" fill="none"/></svg></div>
<div class="abs arrow" style="left:803px"><svg width="8" height="10"><path d="M2 1 L6 5 L2 9" stroke="#fff" stroke-width="2" fill="none"/></svg></div>

<div class="abs section-head">
  <h2><em>Coaster</em> Products Avaiable For</h2>
  <p>Lorem ispum is the dummy text of the industry Lorem ispum is the dummy text of the industry</p>
</div>
<div class="abs rule"></div>
<div class="abs stars">★★★</div>

<!-- row 1 -->
<div class="photo" style="left:104px;top:459px;width:145px;height:120px;background:linear-gradient(180deg,#b7a98a 0%,#9d8d70 55%,#b3262a 70%,#8a1c1c 100%)" role="img" aria-label="Gift shop storefront"></div>
<div class="tile" style="left:249px;top:459px;width:168px;height:120px;background:var(--green);color:#222">
  <h3>For Shops</h3><p>A wide selection of stock gifts plus custom-made souvenirs for retailers.</p><span class="go" style="color:#fff"></span></div>
<div class="photo" style="left:417px;top:459px;width:145px;height:120px;background:linear-gradient(90deg,#8a8470 0%,#c8c0a8 40%,#d9c7b5 60%,#7a6a60 100%)" role="img" aria-label="Artist beside his painting"></div>
<div class="tile" style="left:562px;top:459px;width:168px;height:120px;background:var(--red);color:#fff">
  <h3>For Artists</h3><p>Extend your range of products and increase your profitability.</p><span class="go"></span></div>

<!-- row 2 -->
<div class="tile" style="left:104px;top:579px;width:168px;height:121px;background:var(--charcoal);color:#fff">
  <h3>For Business</h3><p>Promotions &amp; gifts to help you get more business</p><span class="go"></span></div>
<div class="photo" style="left:272px;top:579px;width:145px;height:121px;background:linear-gradient(160deg,#dfe8ef 0%,#9fb3c4 50%,#4a5a6c 100%)" role="img" aria-label="Business handshake"></div>
<div class="tile" style="left:417px;top:579px;width:168px;height:121px;background:var(--orange);color:#fff">
  <h3 style="margin-left:10px">For Clubs &amp; Military Units</h3><p style="margin-left:10px">Custom made regalia and fundraising products</p><span class="go"></span></div>
<div class="photo" style="left:585px;top:579px;width:145px;height:121px;background:linear-gradient(120deg,#2c3e6a 0%,#8a9cc0 45%,#c3c8d8 60%,#b22234 100%)" role="img" aria-label="Saluting soldier before a flag"></div>

<!-- row 3 -->
<div class="photo" style="left:104px;top:700px;width:169px;height:120px;background:linear-gradient(135deg,#f19ab8 0%,#e35c8c 60%,#d4a020 100%)" role="img" aria-label="Flexible pink coaster product promotion">
  <div class="caption">For Individuals<span class="go"></span></div></div>
<div class="photo" style="left:273px;top:700px;width:145px;height:120px;background:linear-gradient(180deg,#8a9c88 0%,#b7a896 45%,#c43c6a 70%,#3a7ab8 100%)" role="img" aria-label="School children holding their artwork">
  <div class="caption">Fundraising For Schools<span class="go"></span></div></div>
<div class="photo" style="left:418px;top:700px;width:312px;height:120px;background:radial-gradient(circle at 50% 55%,#2a3560 0%,#0d0a14 45%,#1a0508 100%)" role="img" aria-label="Video: illuminated glowing coasters under a glass"></div>

<!-- welcome -->
<section class="abs welcome">
  <h2 class="block-title"><em>Welcome To The Brindel</em> Works</h2>
  <p style="margin-top:14px">We offer stock items as well as specialising in custom manufacture and can offer our products customised for virtually any task or occasion. The main areas we service are outlined below. However we are not ‘blinkered’ to these areas and are keen to offer our services to anyone who might need them. A new and different project is always something we relish.</p>
  <p>We are a UK manufacturer of a wide variety of mat &amp; gift products.</p>
  <p class="strong">See our special range of Wedding favours and mementos.</p>
  <p class="tagline">UK Manufacturer of Quality Products For 15 Years</p>
  <p class="more">Read More</p>
</section>
<div class="abs divider"></div>
<section class="abs inquiry">
  <h2 class="block-title"><em>Quick</em> Inquiry</h2>
  <div class="field first">Name</div>
  <div class="field">Email</div>
  <div class="field">Phone</div>
  <div class="field msg">Message</div>
  <div class="submit">SUBMIT</div>
</section>

<footer class="abs footer">
  <div class="footnav"><span>HOME</span><span>FOR INDIVIDUALS</span><span>FOR BUSINESSES</span><span>FOR SHOPS</span><span>FOR CLUBS</span><span>FOR ARTISTS</span><span>CONTACT US</span></div>
  <div class="foot-rule"></div>
  <div class="address">The Brindel Works<br>Street Name City Name<br>State Zip code</div>
  <div class="contacts">
    <div><svg width="10" height="10" viewBox="0 0 10 10"><path d="M2 1 L4 1 L5 3 L4 4 Q5 6 6 6 L7 5 L9 6 L9 8 Q5 9 1 3 Z" fill="#bbb"/></svg>123-456-7890</div>
    <div><svg width="10" height="10" viewBox="0 0 10 10"><rect x="1" y="4" width="8" height="4" fill="#bbb"/><rect x="3" y="1" width="4" height="3" fill="#bbb"/></svg>123-456-7890</div>
    <div><svg width="10" height="10" viewBox="0 0 10 10"><rect x="1" y="2.5" width="8" height="5.5" fill="#bbb"/><path d="M1 2.5 L5 6 L9 2.5" stroke="#1f1f1f" fill="none"/></svg>inquiry@brindelworks.example</div>
  </div>
  <div class="email-in">Enter Your Email Here</div>
  <div class="subscribe">SUBSCRIBE</div>
  <div class="foot-logo">The Brindel<br>Works</div>
</footer>
<div class="abs legal">
  <p>Copyright © 2015 TheBrindelWorks &nbsp;| &nbsp; All Rights Reserved &nbsp;| &nbsp; Terms &amp; Conditions</p>
  <div class="social"><span></span><span></span><span></span></div>
</div>

</body>
</html>
```